Bref créative
Valcourt Chiropractic
Business card, letterhead, envelope
Professional
Valcourt Chiropractic (use logo)
41785 Brookhaven Rd
Oakridge Twp, MI 48193
info@ValcourtChiroExample.com
www.ValcourtChiroExample.com
Want a design that portrays health and wellness in a professional manner
(in bullet format)
-We Specialize in Improving Health & Wellness Naturally
-Most Insurances Accepted
-Holistic Family Health Care
-Massage Therapist on Staff

```html
<!DOCTYPE html>
<html lang="en">
<head>
<meta charset="utf-8">
<title>Valcourt Chiropractic – Business Cards</title>
<link rel="stylesheet" href="https://fonts.googleapis.com/css2?family=Cinzel:wght@400;600&display=swap">
<style>
  :root {
    --page: #ffffff;
    --green: #3c9a2e;
    --green-dark: #1f6d24;
    --green-light: #b9c934;
    --blue: #1f3f9c;
    --blue-dark: #18267a;
    --blue-light: #2c6fc0;
    --white: #ffffff;
    --ink: #2f5a2a;
    --edge: #c9c9c9;
  }
  * { box-sizing: border-box; margin: 0; padding: 0; }
  html, body { width: 1200px; height: 715px; overflow: hidden; background: var(--page); }
  body { position: relative; font-family: "Cinzel", "Times New Roman", serif; }

  .card {
    position: absolute;
    width: 581px;
    height: 324px;
    overflow: hidden;
    border: 1px solid var(--edge);
  }
  .card--front-swoosh { left: 12px; top: 29px; background: var(--white); }
  .card--back-green { left: 607px; top: 29px;
    background: radial-gradient(ellipse at 45% 45%, var(--green-light) 0%, var(--green) 55%, var(--green-dark) 100%); }
  .card--front-white { left: 12px; top: 367px; background: var(--white); }
  .card--back-blue { left: 607px; top: 367px;
    background: radial-gradient(ellipse at 55% 55%, var(--blue-light) 0%, var(--blue) 50%, var(--blue-dark) 100%); }

  .swoosh { position: absolute; inset: 0; width: 100%; height: 100%; }

  .brand {
    position: absolute;
    display: flex;
    align-items: center;
    gap: 14px;
    color: var(--blue);
    font-weight: 600;
    line-height: 1.05;
  }
  .brand__dot { flex: none; border-radius: 50%; background: var(--green); }
  .brand--corner { left: 36px; top: 24px; font-size: 30px; }
  .brand--corner .brand__dot { width: 62px; height: 62px; }
  .brand--center { left: 0; right: 0; top: 108px; justify-content: center; font-size: 38px; }
  .brand--center .brand__dot { width: 80px; height: 80px; }

  .card__title {
    position: absolute; left: 36px; top: 140px;
    color: var(--white); font-size: 20px; font-weight: 400;
  }
  .contact {
    position: absolute; right: 20px; top: 212px;
    color: var(--white); text-align: right;
    font-size: 11px; line-height: 18px; letter-spacing: 0.3px;
  }

  .services {
    position: absolute; list-style: none;
    font-size: 15px; line-height: 22px;
  }
  .services--light { left: 24px; top: 8px; color: var(--white); }
  .services--dark { left: 0; right: 0; top: 228px; text-align: center; color: var(--ink); font-size: 14.5px; line-height: 21px; }

  .mark {
    position: absolute;
    display: flex; align-items: center; justify-content: center;
    border-radius: 50%;
    background: var(--white);
    color: var(--blue);
    font-weight: 600; text-align: center; line-height: 1.1;
  }
  .mark--green { left: 417px; top: 115px; width: 168px; height: 168px; font-size: 17px; }
  .mark--blue { left: 383px; top: 119px; width: 180px; height: 180px; font-size: 18px; }
</style>
</head>
<body>

  <section class="card card--front-swoosh" aria-label="Card front with contact details">
    <svg class="swoosh" viewBox="0 0 581 324" preserveAspectRatio="none" aria-hidden="true">
      <defs>
        <linearGradient id="swooshGreen" x1="0" y1="0" x2="1" y2="1">
          <stop offset="0" stop-color="#4aa83a"/>
          <stop offset="1" stop-color="#1f6d24"/>
        </linearGradient>
      </defs>
      <path d="M0,132 C210,138 420,96 581,-8 L581,324 L0,324 Z" fill="var(--blue)"/>
      <path d="M0,146 C210,150 430,110 581,8 L581,324 L0,324 Z" fill="url(#swooshGreen)"/>
    </svg>
    <div class="brand brand--corner">
      <span class="brand__dot"></span>
      <span>Valcourt<br>Chiropractic</span>
    </div>
    <h2 class="card__title">Valcourt Chiropractic</h2>
    <address class="contact">
      41785 Brookhaven Rd. Oakridge Twp, MI 48193<br>
      Phone: (555)014-9248 | Fax: (555)014-6048<br>
      Email: info@ValcourtChiroExample.com<br>
      www.ValcourtChiroExample.com
    </address>
  </section>

  <section class="card card--back-green" aria-label="Card back with services">
    <ul class="services services--light">
      <li>-We Specialize in Improving Health &amp; Wellness Naturally</li>
      <li>-Most Insurances Accepted</li>
      <li>-Holistic Family Health Care</li>
      <li>-Massage Therapist on Staff</li>
    </ul>
    <div class="mark mark--green">Valcourt<br>Chiropractic</div>
  </section>

  <section class="card card--front-white" aria-label="Card front with services">
    <div class="brand brand--center">
      <span class="brand__dot"></span>
      <span>Valcourt<br>Chiropractic</span>
    </div>
    <ul class="services services--dark">
      <li>-We Specialize in Improving Health &amp; Wellness Naturally</li>
      <li>-Most Insurances Accepted</li>
      <li>-Holistic Family Health Care</li>
      <li>-Massage Therapist on Staff</li>
    </ul>
  </section>

  <section class="card card--back-blue" aria-label="Card back with services, blue">
    <ul class="services services--light">
      <li>-We Specialize in Improving Health &amp; Wellness Naturally</li>
      <li>-Most Insurances Accepted</li>
      <li>-Holistic Family Health Care</li>
      <li>-Massage Therapist on Staff</li>
    </ul>
    <div class="mark mark--blue">Valcourt<br>Chiropractic</div>
  </section>

</body>
</html>
```